Corvane Electronics, Inc. Business card

Incorporate a globe.
We repair electronics, sell electronic parts, and we recycle electronics. We've been in business since 1982. A technology feel to the card is preferred. I want to be able to give this card to a client from different industries and make it relate-able. I don't have a logo that I've been partial to in the past. It is not necessary in this case.

Target Market(s)

Consumer, Industrial, Business, Medical

Industry/Entity Type

Business

Contact Information for Business Card

4518 Maple Crest Blvd. Dallas, TX 75207
214-555-0187 main 214-555-0143 fax
Paul Bredesen VP

Font styles to use
Serif

Requirements
Must have
• Technology feel
Nice to have
• Metallic look
Should not have
• no pastel colors

```html
<!DOCTYPE html>
<html lang="en">
<head>
<meta charset="utf-8">
<title>Corvane Electronics, Inc. – Business Card</title>
<link rel="stylesheet" href="https://fonts.googleapis.com/css2?family=Raleway:wght@500&family=Noto+Serif:wght@400&display=swap">
<style>
  :root {
    --stage: #000000;
    --panel-dark: #242a31;
    --panel-light: #f3f3f3;
    --accent: #0a9be0;
    --name: #ffffff;
    --ink: #222222;
    --globe-light: #3d444c;
    --globe-dark: #30363d;
  }
  * { margin: 0; padding: 0; box-sizing: border-box; }
  html, body {
    width: 1200px; height: 720px; overflow: hidden;
    background: var(--stage);
  }
  .card {
    position: absolute; left: 38px; top: 39px;
    width: 1121px; height: 640px;
    background: var(--panel-light);
    overflow: hidden;
  }
  .brand-panel {
    position: absolute; left: 0; top: 0;
    width: 558px; height: 640px;
    background: var(--panel-dark);
    overflow: hidden;
  }
  .accent-dash {
    position: absolute; height: 8px; background: var(--accent);
  }
  .accent-dash--top { left: 0; top: 29px; width: 57px; }
  .accent-dash--bottom { right: 0; top: 603px; width: 60px; }
  .accent-bar {
    position: absolute; left: 558px; top: 79px;
    width: 11px; height: 475px; background: var(--accent);
  }
  .brand-mark {
    position: absolute; left: 228px; top: 155px;
    width: 86px; height: 86px; border-radius: 50%;
    background: var(--name);
  }
  .brand-name {
    position: absolute; left: 0; top: 262px; width: 558px;
    text-align: center;
    font-family: "Raleway", sans-serif; font-weight: 500;
    font-size: 50px; line-height: 62px;
    color: var(--name);
    text-transform: uppercase;
    letter-spacing: -0.5px;
  }
  .globe {
    position: absolute; left: -96px; top: 462px;
    width: 192px; height: 192px; border-radius: 50%;
    background: radial-gradient(circle at 40% 35%, var(--globe-light), var(--globe-dark));
    transform: translateX(96px);
  }
  .contact-list {
    position: absolute; left: 656px; top: 219px;
    list-style: none;
  }
  .contact-item {
    display: flex; align-items: flex-start;
    height: 64px;
  }
  .contact-icon {
    flex: none; width: 48px; height: 48px;
    border-radius: 8px; background: var(--accent);
    display: flex; align-items: center; justify-content: center;
  }
  .contact-text {
    margin-left: 21px; padding-top: 8px;
    font-family: "Noto Serif", serif; font-size: 20px;
    line-height: 27px; color: var(--ink);
  }
</style>
</head>
<body>
  <div class="card">
    <div class="brand-panel">
      <div class="accent-dash accent-dash--top"></div>
      <div class="brand-mark"></div>
      <div class="brand-name">Corvane<br>Electronics</div>
      <div class="globe" role="img" aria-label="Globe showing the Americas"></div>
    </div>
    <div class="accent-bar"></div>
    <div class="accent-dash accent-dash--bottom"></div>

    <ul class="contact-list">
      <li class="contact-item">
        <span class="contact-icon">
          <svg width="26" height="26" viewBox="0 0 24 24" aria-hidden="true">
            <path fill="#fff" d="M6.6 10.8c1.4 2.8 3.8 5.1 6.6 6.6l2.2-2.2c.3-.3.7-.4 1-.2 1.1.4 2.3.6 3.6.6.6 0 1 .4 1 1V20c0 .6-.4 1-1 1C10.6 21 3 13.4 3 4c0-.6.4-1 1-1h3.5c.6 0 1 .4 1 1 0 1.3.2 2.5.6 3.6.1.3 0 .7-.2 1z"/>
          </svg>
        </span>
        <span class="contact-text">214-555-0187</span>
      </li>
      <li class="contact-item">
        <span class="contact-icon">
          <svg width="28" height="28" viewBox="0 0 24 24" aria-hidden="true">
            <rect x="7" y="3" width="10" height="5" fill="#fff"/>
            <rect x="3" y="9" width="18" height="8" rx="2" fill="#fff"/>
            <rect x="7" y="13" width="10" height="8" fill="#fff" stroke="#0a9be0" stroke-width="1.2"/>
            <line x1="9" y1="16" x2="15" y2="16" stroke="#0a9be0" stroke-width="1.2"/>
            <line x1="9" y1="18.5" x2="15" y2="18.5" stroke="#0a9be0" stroke-width="1.2"/>
          </svg>
        </span>
        <span class="contact-text">214-555-0143</span>
      </li>
      <li class="contact-item">
        <span class="contact-icon">
          <svg width="26" height="28" viewBox="0 0 24 26" aria-hidden="true">
            <path fill="none" stroke="#fff" stroke-width="2" d="M12 24s-7-7.5-7-13a7 7 0 0 1 14 0c0 5.5-7 13-7 13z"/>
            <circle cx="12" cy="11" r="2.6" fill="none" stroke="#fff" stroke-width="2"/>
          </svg>
        </span>
        <span class="contact-text">4518 Maple Crest Blvd. Dallas,<br>TX 75207</span>
      </li>
    </ul>
  </div>
</body>
</html>
```